Church Christmas Flyer

The flyer is to advertise our Christmas Eve services. The flyer is for a Christian church service to celebrate the birth of Jesus. We would like to see designs that use blue, silver and gold for colors but feel free to be creative. We are interested in a flyer that is has texture, depth and is more abstract than literal. Don't be afraid to layer. Please make the flyer double sided

* I uploaded our Christmas flyer from last year.

Target Market(s)

30-55 year old, male and female

Industry/Entity Type

Church

Requirements
Must have
• Map to the church
Church phone number 555-314-7096
Service times 3:00pm and 5:00pm
church address 28315 Marigold Ave, Hesperia, Ca. 92345
church website www.brookstonefellowship.example
Scripture verse

Text must stand out and be easy to read
Nice to have
• Use of the star in the sky that guided the wise men to Jesus.
Should not have
• Santa Clause, Snowmen, Reindeer

```html
<!DOCTYPE html>
<html lang="en">
<head>
<meta charset="utf-8">
<title>Christmas Eve Flyer – Brookstone Fellowship</title>
<link rel="stylesheet" href="https://fonts.googleapis.com/css2?family=Arimo:wght@400;700&family=Oswald:wght@200;300;400&display=swap">
<style>
  :root {
    --navy: #1d4a84;
    --white: #ffffff;
    --gold: #c79b3b;
    --quote: #e6e9ef;
    --page: #e9eaec;
  }
  html, body {
    margin: 0;
    width: 1200px;
    height: 1064px;
    overflow: hidden;
    background: var(--page);
  }
  .flyer-side {
    position: absolute;
    left: 21px;
    width: 1158px;
    height: 468px;
    display: block;
  }
  .flyer-side--front { top: 37px; }
  .flyer-side--back { top: 561px; }

  .title { font-family: "Arimo", Arial, sans-serif; font-size: 58px; fill: var(--navy); }
  .tagline { font-family: "Arimo", Arial, sans-serif; font-size: 19px; fill: var(--gold); letter-spacing: 0.3px; }
  .side-name { font-family: "Arimo", Arial, sans-serif; font-size: 12px; fill: var(--white); letter-spacing: 0.6px; }

  .verse { font-family: "Oswald", "Arial Narrow", sans-serif; font-weight: 200; fill: var(--quote); }
  .verse-lead { font-size: 60px; }
  .verse-body { font-size: 30px; }
  .verse-accent { font-size: 40px; }
  .quote-mark { font-family: "Arimo", Arial, sans-serif; font-size: 100px; font-weight: 700; fill: var(--white); }

  .services-heading { font-family: "Oswald", "Arial Narrow", sans-serif; font-weight: 200; font-size: 57px; fill: var(--white); }
  .services-time { font-family: "Oswald", "Arial Narrow", sans-serif; font-weight: 400; font-size: 29px; fill: var(--white); }
  .church-name { font-family: "Oswald", "Arial Narrow", sans-serif; font-weight: 400; font-size: 30px; fill: var(--white); }
  .church-address { font-family: "Oswald", "Arial Narrow", sans-serif; font-weight: 300; font-size: 27px; fill: var(--white); }
  .contact-phone { font-family: "Arimo", Arial, sans-serif; font-size: 26px; fill: var(--navy); }
  .contact-web { font-family: "Arimo", Arial, sans-serif; font-size: 22px; fill: var(--navy); }
  .map-area { fill: rgba(255,255,255,0.08); stroke: rgba(255,255,255,0.35); stroke-width: 1; }
</style>
</head>
<body>

<svg class="flyer-side flyer-side--front" viewBox="0 0 1158 468" role="group" aria-label="Flyer front">
  <defs>
    <radialGradient id="front-glow" cx="0.15" cy="1" r="1.05">
      <stop offset="0" stop-color="#d7dbe3"/>
      <stop offset="0.35" stop-color="#9aa8c2"/>
      <stop offset="0.7" stop-color="#3d5f92"/>
      <stop offset="1" stop-color="#1d4a84"/>
    </radialGradient>
  </defs>
  <rect class="card-base" width="1158" height="468" fill="var(--navy)"/>
  <rect class="white-field" width="1158" height="228" fill="var(--white)"/>
  <path class="night-sky" d="M45 468 C150 250 450 60 915 0 H1158 V468 Z" fill="url(#front-glow)"
        role="img" aria-label="Soft blue night sky with faint silhouettes of the wise men on camels beneath the star"/>

  <text class="title" x="40" y="85">CHRISTMAS EVE</text>
  <text class="tagline" x="41" y="115">A CELEBRATION OF GOD’S LOVE</text>
  <text class="side-name" transform="translate(26 455) rotate(-90)">BROOKSTONE FELLOWSHIP</text>

  <text class="quote-mark" x="442" y="361">“</text>
  <text class="verse verse-lead" x="499" y="352" textLength="529" lengthAdjust="spacing">This is how god showed</text>
  <text class="verse verse-body" x="493" y="384" textLength="583" lengthAdjust="spacing">his <tspan class="verse-accent">love</tspan> among us. He sent his one and <tspan class="verse-accent">only</tspan> son</text>
  <text class="verse verse-body" x="493" y="420" textLength="451" lengthAdjust="spacing">into the world that might live through him.</text>
  <text class="quote-mark" x="946" y="480">”</text>
</svg>

<svg class="flyer-side flyer-side--back" viewBox="0 0 1158 468" role="group" aria-label="Flyer back">
  <defs>
    <radialGradient id="back-glow" cx="0.85" cy="1" r="1.05">
      <stop offset="0" stop-color="#d7dbe3"/>
      <stop offset="0.35" stop-color="#9aa8c2"/>
      <stop offset="0.7" stop-color="#3d5f92"/>
      <stop offset="1" stop-color="#1d4a84"/>
    </radialGradient>
  </defs>
  <rect class="card-base" width="1158" height="468" fill="var(--navy)"/>
  <rect class="white-field" width="1158" height="239" fill="var(--white)"/>
  <path class="night-sky" d="M1105 468 C1000 250 708 60 265 0 H0 V468 Z" fill="url(#back-glow)"
        role="img" aria-label="Soft blue night sky with faint silhouettes of the wise men on camels beneath the star"/>

  <text class="title" x="1118" y="88" text-anchor="end">CHRISTMAS EVE</text>
  <text class="tagline" x="1116" y="117" text-anchor="end">A CELEBRATION OF GOD’S LOVE</text>
  <text class="side-name" transform="translate(1126 250) rotate(90)">BROOKSTONE FELLOWSHIP</text>

  <text class="services-heading" x="70" y="193" textLength="589" lengthAdjust="spacing">CHRISTMAS EVE SERVICES</text>
  <text class="services-time" x="71" y="230" textLength="594" lengthAdjust="spacing">DECEMBER 24TH 2011 AT 3.00PM AND 5.00PM</text>

  <text class="church-name" x="71" y="338" textLength="408" lengthAdjust="spacing">BROOKSTONE FELLOWSHIP</text>
  <text class="church-address" x="71" y="374">28315 MARIGOLD AVE, HESPERIA</text>

  <rect class="map-area" x="482" y="240" width="298" height="150"
        role="img" aria-label="Street map showing the church location near Marigold Ave"/>

  <text class="contact-phone" x="1050" y="393" text-anchor="end">555-314-7096</text>
  <text class="contact-web" x="1050" y="421" text-anchor="end">www.brookstonefellowship.example</text>
</svg>

</body>
</html>
```